Business Card Design

I already have a company logo for my company. I have a logo for the manufacturer we represent. I want a professional business card design.

```html
<!DOCTYPE html>
<html lang="en">
<head>
<meta charset="UTF-8">
<title>Signalguard Partners — Business Card</title>
<link href="https://fonts.googleapis.com/css2?family=Montserrat:wght@400;500;700&display=swap" rel="stylesheet">
<style>
  :root {
    --bg: #3a3a3c;
    --card-front: #e4e4e4;
    --card-back: #ffffff;
    --red: #e0262b;
    --gold: #b58f1f;
    --black: #111111;
    --gray-band: #d5d5d5;
    --ink: #2a2a2a;
  }
  * { margin: 0; padding: 0; box-sizing: border-box; }
  html, body { width: 1200px; height: 688px; overflow: hidden; }
  body {
    background: var(--bg);
    font-family: "Montserrat", sans-serif;
    position: relative;
  }
  .card {
    position: absolute;
    top: 196px;
    width: 520px;
    height: 297px;
    box-shadow: 0 10px 28px rgba(0,0,0,.45);
    overflow: hidden;
  }
  .card-front { left: 50px; background: var(--card-front); }
  .card-back { left: 630px; background: var(--card-back); }

  .brand {
    display: flex;
    align-items: center;
    gap: 10px;
    color: var(--red);
    font-weight: 700;
    text-transform: uppercase;
    line-height: 1.1;
  }
  .brand-dot {
    flex: none;
    border-radius: 50%;
    background: var(--red);
  }
  .card-front .brand {
    position: absolute;
    left: 50%; top: 50%;
    transform: translate(-50%, -50%);
    font-size: 26px;
  }
  .card-front .brand-dot { width: 22px; height: 22px; }

  .card-back .brand {
    position: absolute;
    left: 34px; top: 118px;
    width: 200px;
    font-size: 17px;
  }
  .card-back .brand-dot { width: 16px; height: 16px; }

  .contact {
    position: absolute;
    left: 262px; top: 62px;
    padding-left: 14px;
    border-left: 2px solid var(--red);
    color: var(--ink);
    font-size: 11.5px;
    line-height: 1.45;
  }
  .contact-name { color: var(--red); font-weight: 700; font-size: 19px; line-height: 1.2; }
  .contact-title { font-size: 12px; margin-bottom: 12px; }
  .contact-address { margin-bottom: 12px; }
  .contact-line { display: flex; align-items: center; gap: 6px; }
  .contact-line svg { width: 10px; height: 10px; fill: var(--red); flex: none; }

  .band {
    position: absolute;
    left: 0; bottom: 0;
    width: 100%; height: 12px;
    display: flex;
  }
  .band span { height: 100%; }
  .band-gray { width: 30%; background: var(--gray-band); }
  .band-black { width: 32%; background: var(--black); }
  .band-red { width: 24%; background: var(--red); }
  .band-gold { width: 14%; background: var(--gold); }
</style>
</head>
<body>
  <section class="card card-front">
    <div class="brand"><span class="brand-dot"></span>Signalguard Partners LLC</div>
  </section>

  <section class="card card-back">
    <div class="brand"><span class="brand-dot"></span>Signalguard Partners LLC</div>
    <div class="contact">
      <div class="contact-name">Daniel Hart</div>
      <div class="contact-title">Managing Director</div>
      <div class="contact-address">2240 Marlow Ave<br>Denver, CO 80206</div>
      <div class="contact-line">
        <svg viewBox="0 0 10 10"><path d="M2 0.5l2 2-1 1.2c.6 1.3 1.6 2.3 2.9 2.9l1.2-1 2 2-1.3 1.8C4 9 1 6 .6 1.8z"/></svg>
        555.210.4836
      </div>
      <div class="contact-line">
        <svg viewBox="0 0 10 10"><path d="M0 2h10v6H0z M0 2l5 3.5L10 2" /></svg>
        info@signalguardllc.com
      </div>
      <div class="contact-line">
        <svg viewBox="0 0 10 10"><circle cx="5" cy="5" r="4.5"/></svg>
        www.signalguardllc.com
      </div>
    </div>
    <div class="band">
      <span class="band-gray"></span><span class="band-black"></span><span class="band-red"></span><span class="band-gold"></span>
    </div>
  </section>
</body>
</html>
```